Postcard needed for expert witness service

Looking for a professional postcard that will be mailed to personal injury lawyers / law firms to introduce my expert witness services.

Target Market(s)

Law firms, personal injury lawyers

Industry/Entity Type

Expert witness, law

Font styles to use
Sans Serif

Requirements
Must have
• Logo: The Frost Counsel [Main Heading]Do you handle snow and ice related slip and falls? Darrel is one of the top snow industry experts in the country! [Following should be in a list type fashion, possibly bulleted]Darrel's credentials: Accredited Winter Practitioner (AWP), past WRTA board member and chair, former ISO 9001 certified snow company owner , 32 years in the industry. (555) 284-3917 NOTES: Postcard will be 4" x 6" Please use both sides however must have room for labels and stamp
Should not have
• Wouldn't suggest using both photos on same side. Honestly, feel free to only use one of the slip and fall photos if it works out better. Thanks!

```html
<!DOCTYPE html>
<html lang="en">
<head>
<meta charset="utf-8">
<title>The Frost Counsel – Postcard</title>
<link rel="stylesheet" href="https://fonts.googleapis.com/css2?family=Bebas+Neue&family=Montserrat:wght@400;500;600&display=swap">
<style>
  :root {
    --backdrop: #3a3a3a;
    --paper: #ffffff;
    --ink: #000000;
    --gold: #cdb485;
    --rule: #8a8a8a;
  }
  * { margin: 0; padding: 0; box-sizing: border-box; }
  html, body { width: 914px; height: 1200px; overflow: hidden; }
  body { background: var(--backdrop); position: relative; font-family: "Montserrat", sans-serif; }

  .card { position: absolute; left: 100px; width: 715px; height: 476px; background: var(--paper); overflow: hidden; }
  .card--front { top: 99px; }
  .card--back { top: 625px; }
  .card > * { position: absolute; }
  .card svg.shapes { left: 0; top: 0; width: 715px; height: 476px; }

  .logo { font-family: "Montserrat", sans-serif; font-weight: 400; color: var(--ink); text-align: center; line-height: 1; }
  .logo__top { display: block; font-size: 29px; letter-spacing: 1px; }
  .logo__bottom { display: block; font-size: 16px; letter-spacing: 2px; margin-top: 6px; }
  .card--front .logo { left: 27px; top: 27px; width: 186px; }
  .card--back .logo { left: 514px; top: 400px; width: 163px; }
  .card--back .logo__top { font-size: 27px; }
  .card--back .logo__bottom { font-size: 15px; margin-top: 4px; }

  .headline { font-family: "Bebas Neue", sans-serif; font-weight: 400; line-height: 42px; font-size: 52px; left: 27px; top: 112px; }
  .headline span { display: block; }
  .gold { color: var(--gold); }
  .dark { color: var(--ink); }

  .intro { font-weight: 500; font-size: 16px; line-height: 18px; color: var(--ink); left: 27px; top: 245px; width: 290px; }
  .card--back .intro { color: var(--paper); top: 270px; }

  .credentials { left: 27px; top: 321px; width: 430px; font-size: 11.6px; line-height: 15px; color: var(--paper); font-weight: 400; list-style: none; }

  .cta { left: 27px; top: 390px; }
  .card--back .cta { top: 385px; }
  .cta__label { font-size: 19px; font-weight: 500; color: var(--ink); line-height: 22px; }
  .card--back .cta__label { color: var(--paper); }
  .cta__phone { font-family: "Bebas Neue", sans-serif; font-size: 44px; line-height: 44px; color: var(--gold); margin-top: 3px; letter-spacing: 0.5px; }

  .back-heading { left: 27px; top: 50px; font-family: "Bebas Neue", sans-serif; color: var(--paper); font-size: 35px; line-height: 28px; }
  .back-heading span { display: block; }
  .back-title { left: 24px; top: 119px; font-family: "Bebas Neue", sans-serif; color: var(--gold); font-size: 78px; line-height: 67px; }
  .back-title span { display: block; }
</style>
</head>
<body>

<section class="card card--front">
  <svg class="shapes" viewBox="0 0 715 476" aria-hidden="false">
    <defs>
      <linearGradient id="front-photo-tone" x1="0" y1="0" x2="0" y2="1">
        <stop offset="0" stop-color="#a9a5a3"/>
        <stop offset="0.45" stop-color="#4b5e80"/>
        <stop offset="1" stop-color="#6f6d6c"/>
      </linearGradient>
    </defs>
    <polygon points="512,0 715,0 715,476 367,476" fill="url(#front-photo-tone)" role="img" aria-label="Photo of a person slipping and falling on an icy pavement"/>
    <polygon points="488,0 493,0 415,244 409,244" fill="var(--gold)"/>
    <polygon points="496,0 512,0 428,271 412,271" fill="var(--ink)"/>
    <polygon points="0,319 484,319 466,372 0,372" fill="var(--ink)"/>
    <circle cx="318" cy="422" r="34" fill="var(--gold)"/>
  </svg>

  <div class="logo"><span class="logo__top">THE FROST</span><span class="logo__bottom">COUNSEL</span></div>

  <h1 class="headline">
    <span class="gold">Do you handle</span>
    <span class="dark">Snow and ice related</span>
    <span class="gold">Slip and falls?</span>
  </h1>

  <p class="intro">Darrel is one of the top snow industry experts in the country!</p>

  <ul class="credentials">
    <li>Darrel's credentials: Accredited Winter Practitioner (AWP), past WRTA board member and chair, former ISO 9001 certified snow company owner , 32 years in the industry.</li>
  </ul>

  <div class="cta">
    <p class="cta__label">Call Now Today!</p>
    <p class="cta__phone">(555) 284-3917</p>
  </div>
</section>

<section class="card card--back">
  <svg class="shapes" viewBox="0 0 715 476">
    <defs>
      <linearGradient id="back-photo-tone" x1="0" y1="0" x2="1" y2="1">
        <stop offset="0" stop-color="#9d978f"/>
        <stop offset="0.5" stop-color="#4f5a6b"/>
        <stop offset="1" stop-color="#d9d9d6"/>
      </linearGradient>
    </defs>
    <polygon points="0,0 437,0 290,476 0,476" fill="var(--ink)"/>
    <polygon points="344,82 510,82 466,254 290,254" fill="url(#back-photo-tone)" role="img" aria-label="Photo of a woman who has fallen on a snowy path"/>
    <rect x="581.5" y="35.5" width="100" height="100" fill="none" stroke="var(--rule)" stroke-width="1"/>
    <line x1="511" y1="171.5" x2="681" y2="171.5" stroke="var(--rule)" stroke-width="1"/>
    <line x1="511" y1="196.5" x2="681" y2="196.5" stroke="var(--rule)" stroke-width="1"/>
    <line x1="511" y1="221.5" x2="681" y2="221.5" stroke="var(--rule)" stroke-width="1"/>
  </svg>

  <h2 class="back-heading"><span>What accident lawyers</span><span>want you to know about</span></h2>
  <p class="back-title"><span>Slip &amp; Fall</span><span>Accident</span></p>

  <p class="intro">Darrel is one of the top snow industry experts in the country!</p>

  <div class="cta">
    <p class="cta__label">Call Now Today!</p>
    <p class="cta__phone">(555) 284-3917</p>
  </div>

  <div class="logo"><span class="logo__top">THE FROST</span><span class="logo__bottom">COUNSEL</span></div>
</section>

</body>
</html>
```